Large multi-office optometry business opening a Dry Eye Spa and needs sign.

Business name/sign info: Brenwick Dry Eye Institute, (555) 362-4817
Backlit pole sign at office entrance on a very busy street
Sign dimensions: 53" tall x 136.5" wide
State of the art Dry Eye Spa for treatment of all forms of dry eye and ocular surface disease. Also, have aesthetics treatments (IPL, Low Level Light Treatment, etc.)

Target Market(s)

People who are suffering from: dryness, burning, foreign body sensation, itching, fluctuating vision, tired eyes, etc.

Industry/Entity Type

Optometry and aesthetics

Colors
0054AA
0677BA
7BADD7
CADEEF
E8F1F8

Requirements
Must have
• Business name, phone number, subliminal message of relief in a glance or short look.
Nice to have
• Cool, relief, soothing sense.
Should not have
• Too much information or too busy.

```html
<!DOCTYPE html>
<html lang="en">
<head>
<meta charset="utf-8">
<title>Brenwick Dry Eye Institute – Pole Sign</title>
<link rel="stylesheet" href="https://fonts.googleapis.com/css2?family=Cinzel:wght@700&family=Poppins:wght@600&display=swap">
<style>
  :root {
    --page-bg: #ffffff;
    --sign-bg: #ffffff;
    --brand-deep: #0054aa;
    --brand-mid: #0677ba;
    --brand-light: #7badd7;
    --brand-pale: #cadeef;
    --photo-light: #e6e6e6;
    --photo-mid: #b4b4b4;
    --photo-dark: #7a7a7a;
    --phone-text: #ffffff;
  }
  * { margin: 0; padding: 0; box-sizing: border-box; }
  html, body {
    width: 967px;
    height: 1200px;
    overflow: hidden;
    background: var(--page-bg);
  }
  .canvas {
    position: relative;
    width: 967px;
    height: 1200px;
  }
  .sign {
    position: absolute;
    left: 34px;
    top: 424px;
    width: 900px;
    height: 351px;
    background: var(--sign-bg);
    overflow: hidden;
    box-shadow: 0 6px 28px rgba(0, 0, 0, 0.28);
  }
  .sign__photo {
    position: absolute;
    right: 0;
    top: 0;
    width: 410px;
    height: 100%;
    background:
      radial-gradient(ellipse 90px 70px at 270px 150px, var(--photo-dark), transparent 75%),
      linear-gradient(160deg, var(--photo-light) 0%, var(--photo-mid) 55%, var(--photo-dark) 100%);
    -webkit-mask-image: linear-gradient(90deg, transparent 0%, #000 22%);
            mask-image: linear-gradient(90deg, transparent 0%, #000 22%);
  }
  .sign__band {
    position: absolute;
    left: 0;
    bottom: 0;
    width: 900px;
    height: 130px;
  }
  .practice {
    position: absolute;
    left: 42px;
    top: 44px;
    display: flex;
    align-items: center;
    gap: 10px;
    font-family: "Cinzel", serif;
    font-weight: 700;
    font-size: 24px;
    line-height: 1;
    color: var(--brand-deep);
  }
  .practice__dot {
    width: 16px;
    height: 16px;
    border-radius: 50%;
    background: var(--brand-deep);
  }
  .institute {
    position: absolute;
    left: 42px;
    top: 108px;
    font-family: "Cinzel", serif;
    font-weight: 700;
    line-height: 1;
  }
  .institute__place {
    display: block;
    font-size: 70px;
    color: var(--brand-mid);
    letter-spacing: 1px;
  }
  .institute__type {
    display: block;
    margin-top: 4px;
    font-size: 44px;
    color: var(--brand-light);
    letter-spacing: 0.5px;
  }
  .phone {
    position: absolute;
    left: 42px;
    top: 266px;
    font-family: "Poppins", sans-serif;
    font-weight: 600;
    font-size: 46px;
    line-height: 1.2;
    color: var(--phone-text);
    letter-spacing: 0.5px;
  }
</style>
</head>
<body>
<div class="canvas">
  <section class="sign" aria-label="Brenwick Dry Eye Institute sign">
    <div class="sign__photo" role="img" aria-label="Black and white close-up photo of fingers gently opening a dry, irritated eye"></div>

    <svg class="sign__band" viewBox="0 0 900 130" preserveAspectRatio="none" aria-hidden="true">
      <defs>
        <linearGradient id="bandFade" x1="0" y1="0" x2="1" y2="0">
          <stop offset="0" stop-color="#102a66"/>
          <stop offset="0.35" stop-color="#3a4f86"/>
          <stop offset="0.65" stop-color="#8a9cc4" stop-opacity="0.7"/>
          <stop offset="0.95" stop-color="#cadeef" stop-opacity="0"/>
        </linearGradient>
      </defs>
      <path d="M0 20 C 60 -2, 160 2, 300 14 C 470 30, 620 48, 900 52 L 900 130 L 0 130 Z" fill="url(#bandFade)"/>
    </svg>

    <div class="practice">
      <span class="practice__dot" aria-hidden="true"></span>
      <span class="practice__name">Ellison Family Vision</span>
    </div>

    <h1 class="institute">
      <span class="institute__place">BRENWICK</span>
      <span class="institute__type">DRY EYE INSTITUTE</span>
    </h1>

    <p class="phone">(555) 362-4817</p>
  </section>
</div>
</body>
</html>
```